Simple 1 page layout for addrforge-tool.com

Visit http://addrforge-tool.com

The site calculates ipv6 unique local addresses for free. The content will stay as it is. There's going to be Brelvo promoslots below the red box and at the bottom of the page.

The red box contains the most important information on this page. The users focus should go there immediately.

The contents below composition is also kind of important.

Reason: I'm very busy at the moment. I need more time for evaluation and feedback. Thanks for your contributions and your patience.

Target Market(s)

IT and networking people

Industry/Entity Type

Brelvo

Requirements
Must have
• I need all pieces nicely cut, so I only have to do HTML and CSS.

```html
<!DOCTYPE html>
<html lang="en">
<head>
<meta charset="utf-8">
<title>AddrForge – local network address generator</title>
<link rel="stylesheet" href="https://fonts.googleapis.com/css2?family=Arimo:wght@400;700&family=Courier+Prime:wght@400;700&display=swap">
<style>
:root{
  --bg:#222222;
  --bg-top:#1d1d1d;
  --bg-faq:#242424;
  --line:#111111;
  --line-light:#333333;
  --panel:#191919;
  --panel-edge:#2c2c2c;
  --accent:#e8582a;
  --accent-soft:#e0722e;
  --text:#e6e6e6;
  --text-dim:#cfcfcf;
  --btn-top:#4a4a4a;
  --btn-bottom:#2a2a2a;
  --btn-text:#1a1a1a;
  --green:#6fd04a;
}
*{box-sizing:border-box;margin:0;padding:0}
html,body{width:956px;height:1200px;overflow:hidden}
body{background:var(--bg);font-family:"Arimo",Arial,sans-serif;color:var(--text);position:relative}
.top-band{position:absolute;left:0;top:0;width:956px;height:96px;background:var(--bg-top);border-bottom:1px solid var(--line);box-shadow:0 1px 0 var(--line-light)}
.brand{position:absolute;left:49px;top:63px;width:224px;height:65px;border-radius:6px;background:linear-gradient(#3e3e3e,#262626);border:2px solid #0e0e0e;box-shadow:0 0 0 1px #444 inset,0 3px 6px rgba(0,0,0,.6);padding:9px 0 0 15px}
.brand-name{font-size:21px;font-weight:700;color:var(--accent-soft);line-height:1}
.brand-tag{font-size:12px;color:#f0f0f0;margin-top:8px}
.brand-led{position:absolute;right:6px;top:6px;width:7px;height:7px;border-radius:50%;background:var(--green)}
.nav-btn{position:absolute;top:71px;height:50px;border-radius:8px;background:linear-gradient(var(--btn-top),var(--btn-bottom));border:2px solid #0d0d0d;box-shadow:0 1px 0 #555 inset,0 3px 6px rgba(0,0,0,.6);font-weight:700;font-size:23px;letter-spacing:3px;color:var(--btn-text);text-shadow:0 1px 0 #5a5a5a;display:flex;align-items:center;justify-content:center;text-decoration:none}
.nav-faq{left:580px;width:132px}
.nav-about{left:738px;width:174px}
.result{position:absolute;left:56px;top:162px;width:859px;height:270px;background:var(--panel);border:1px solid var(--panel-edge);border-radius:4px;box-shadow:0 2px 8px rgba(0,0,0,.6)}
.result-pointer{position:absolute;left:160px;top:145px}
.result h2{position:absolute;left:56px;top:20px;font-size:22px;color:#d0d0d0;font-weight:700}
.prefix{position:absolute;left:130px;top:74px;font-size:43px;font-weight:700;color:var(--accent)}
.subnet{position:absolute;left:130px;font-size:17px;font-weight:700;color:var(--text)}
.subnet span{color:var(--accent);font-weight:400;margin-left:12px}
.subnet-first{top:145px}
.subnet-last{top:182px}
.regen{position:absolute;left:617px;top:193px;width:221px;height:61px;border-radius:6px;background:linear-gradient(#2c2c2c,#161616);border:2px solid #080808;box-shadow:0 0 0 1px #3a3a3a inset;color:#ddd}
.regen svg{position:absolute;left:17px;top:13px}
.regen-title{position:absolute;left:80px;top:12px;font-size:17px;color:#e4e4e4}
.regen-sub{position:absolute;left:82px;top:38px;font-size:10.5px;color:#cfcfcf;letter-spacing:.3px}
.regen-led{position:absolute;right:6px;top:5px;width:6px;height:6px;border-radius:50%;border:1px solid #999}
.promo-top{position:absolute;left:130px;top:434px;width:698px;height:99px;background:#141414;border-radius:3px;padding:7px 9px}
.promo-art{width:681px;height:72px;background:linear-gradient(90deg,#e6e6e6 0%,#7a7a7a 20%,#3a3a3a 45%,#5d6d80 62%,#2d2d2d 100%)}
.promo-bar{height:13px;background:#0a0a22;display:flex;justify-content:space-between;font-size:9px;color:#fff;padding:1px 2px;text-decoration:underline}
.section-title{position:absolute;left:112px;font-size:22px;font-weight:700;color:#e2e2e2}
.comp-title{top:580px}
.layout-table{position:absolute;left:184px;top:631px;font-family:"Courier Prime","Courier New",monospace;font-size:12.5px;line-height:18.7px;color:var(--accent-soft);white-space:pre}
.defs{position:absolute;left:186px;top:734px;font-family:"Courier Prime","Courier New",monospace;font-size:12.5px;line-height:18.7px;color:#e8e8e8;white-space:pre}
.defs b{font-weight:700}
.faq-area{position:absolute;left:0;top:862px;width:956px;height:338px;background:var(--bg-faq);border-top:1px solid var(--line);box-shadow:0 1px 0 var(--line-light) inset}
.faq-title{top:898px}
.faq-index{position:absolute;left:113px;top:943px;list-style:none;font-size:11.5px;line-height:18.7px}
.faq-index a{color:var(--accent-soft);text-decoration:none}
.faq-answers{position:absolute;left:336px;top:938px;width:560px}
.faq-answers h3{position:absolute;left:2px;font-size:17px;font-weight:700;color:#eee;white-space:nowrap}
.faq-answers p{position:absolute;left:0;width:560px;font-size:11.3px;line-height:18.7px;color:var(--text-dim)}
</style>
</head>
<body>
<header class="top-band">
  <div class="brand"><div class="brand-name">AddrForge</div><div class="brand-tag">local network address generator</div><span class="brand-led"></span></div>
  <a class="nav-btn nav-faq" href="#faq">FAQ</a>
  <a class="nav-btn nav-about" href="#about">ABOUT US</a>
</header>

<svg class="result-pointer" width="40" height="18" viewBox="0 0 40 18"><path d="M0 18 L20 0 L40 18 Z" fill="#191919" stroke="#2c2c2c"/></svg>
<section class="result">
  <h2>Generated</h2>
  <div class="prefix">fdc5:9fbd:7903::/48</div>
  <div class="subnet subnet-first">First 64-bit subnet <span>fdc5:9fbd:7903::/64</span></div>
  <div class="subnet subnet-last">Last 64-bit subnet <span>fdc5:9fbd:7903:ffff::/64</span></div>
  <div class="regen">
    <svg width="44" height="36" viewBox="0 0 44 36"><g fill="none" stroke="#bbb" stroke-width="3"><path d="M9 14 A14 14 0 0 1 34 12"/><path d="M35 22 A14 14 0 0 1 10 24"/></g><path d="M30 6 L37 13 L28 15 Z M14 30 L7 23 L16 21 Z" fill="#bbb"/><circle cx="22" cy="18" r="5" fill="none" stroke="#888" stroke-width="2"/></svg>
    <div class="regen-title">GET NEW IP</div>
    <div class="regen-sub">Click to regenerate...</div>
    <span class="regen-led"></span>
  </div>
</section>

<aside class="promo-top">
  <div class="promo-art" role="img" aria-label="Promotional banner for a fitness site: athlete and dumbbells with the slogan Be Fit"></div>
  <div class="promo-bar"><span>www.fitpulse-daily.com</span><span>Feedback - Ads by Brelvo</span></div>
</aside>

<h2 class="section-title comp-title">Composition</h2>
<div class="layout-table">| 7 bits |1|  40 bits   |  16 bits  |          64 bits           |
+--------+-+------------+-----------+----------------------------+
| Prefix |L| Global ID  | Subnet ID |        Interface ID        |
+--------+-+------------+-----------+----------------------------+</div>
<div class="defs"><b>Prefix</b>   fc::/7
<b>Local (L)</b>    1
<b>Global ID</b>    c59fbd7903 changes every time you visit this page
<b>Subnet ID</b>    0 - ffff use freely for your own IPv6 subnetting
<b>Interface ID</b> Your host address.</div>

<div class="faq-area"></div>
<h2 class="section-title faq-title" id="faq">F.A.Q</h2>
<ul class="faq-index">
  <li><a href="#">What's a unique local address?</a></li>
  <li><a href="#">What's the use?</a></li>
  <li><a href="#">Why do they need to be unique?</a></li>
  <li><a href="#">Are they really globally unique?</a></li>
  <li><a href="#">Isn't there an easy way?</a></li>
  <li><a href="#">What is the subnet id?</a></li>
  <li><a href="#">Where can I get more information?</a></li>
</ul>
<div class="faq-answers">
  <h3 style="top:0">What's a unique local address?</h3>
  <p style="top:40px">IPv6 unique local addresses are similar to the IPv4 private address classes with one big difference: THE ARE UNIQUE.</p>
  <h3 style="top:113px">What's the use?</h3>
  <p style="top:153px">Local network addresses are used to make specific services only available for people and computers within your private network.<br>For example if your company runs an intranet website containing confidential information about products, sales, customers or what so ever. This information might be vital for your employees to do their jobs, but you definitely don't want to make this website available publicly.</p>
</div>
</body>
</html>
```